Recruitment technology firm needs a downloadable pdf to generate leads.

We need design work for a downloadable pdf that will serve as an educational document to visitors to our website. We help clients identify candidates that fit their job posting. We do that by defining the personality of the job and then assessing the personality of the candidates. We then mathematically compare and rank all the candidates against the job. Our colour scheme is blue. The final design should move from communicating a lack of fit or frustration to people fitting their job and success per the text we have built. People who download this lead generator will be added to our email list for re-marketing purposes. our website is www.tallowridgeadvisory.com. I've attached an example of a lead generator (ebike)for a business unrelated to ours.

Target Market(s)

Our target market is businesses of 50-300 people, we're targeting business owners or executives of entrepreneurial (vs. corporate) companies.

Colors
85acd3
3377b5
0455a3

Requirements
Must have
• Easy to read so text isn't overwhelming.
Nice to have
• Don't be compelled to use our website photos or those like it. I'd like this to reflect entrepreneurial companies, not corporate, suit and tie companies.

```html
<!DOCTYPE html>
<html lang="en">
<head>
<meta charset="utf-8">
<title>5 Reasons You Suck At Hiring For Fit — Tallowridge</title>
<link href="https://fonts.googleapis.com/css2?family=Archivo+Black&family=Montserrat:wght@600;700&display=swap" rel="stylesheet">
<style>
  :root {
    --charcoal: #454545;
    --charcoal-band: #4a4a4a;
    --ocean: #176b98;
    --sky: #27a7dc;
    --white: #ffffff;
    --silver-light: #ffffff;
    --silver-mid: #c9c9c9;
    --silver-dark: #7d7d7d;
  }
  html, body {
    margin: 0;
    padding: 0;
    overflow: hidden;
    background: var(--charcoal);
  }
  .cover {
    position: relative;
    width: 848px;
    height: 1200px;
    overflow: hidden;
    background: var(--charcoal);
  }
  .cover__band {
    position: absolute;
    left: 0;
    top: 120px;
    width: 848px;
    height: 321px;
    background: var(--charcoal-band);
  }
  .cover__shapes {
    position: absolute;
    inset: 0;
  }
  .brand {
    position: absolute;
    left: 58px;
    top: 196px;
    display: flex;
    align-items: center;
    gap: 14px;
  }
  .brand__mark {
    width: 40px;
    height: 40px;
    border-radius: 50%;
    background: var(--sky);
  }
  .brand__name {
    font-family: "Montserrat", sans-serif;
    font-weight: 700;
    font-size: 42px;
    letter-spacing: 1px;
    color: var(--white);
    line-height: 1;
  }
  .tagline {
    position: absolute;
    left: 456px;
    top: 333px;
    width: 420px;
    height: 45px;
    border-radius: 23px 0 0 23px;
    background: var(--sky);
    display: flex;
    align-items: center;
    padding-left: 16px;
    box-sizing: border-box;
    font-family: "Montserrat", sans-serif;
    font-weight: 600;
    font-size: 15px;
    color: var(--white);
    gap: 12px;
  }
  .title {
    position: absolute;
    right: 100px;
    margin: 0;
    font-family: "Archivo Black", sans-serif;
    font-weight: 400;
    line-height: 1;
    text-align: right;
    white-space: nowrap;
    background: linear-gradient(180deg, var(--silver-dark) 0%, var(--silver-light) 45%, var(--silver-mid) 70%, var(--silver-dark) 100%);
    -webkit-background-clip: text;
    background-clip: text;
    color: transparent;
    filter: drop-shadow(2px 3px 1px rgba(0,0,0,0.75));
  }
  .title--reasons { top: 464px; font-size: 114px; letter-spacing: -2px; }
  .title--suck { top: 578px; font-size: 50px; right: 108px; letter-spacing: -1px; }
  .title--fit { top: 630px; font-size: 84px; letter-spacing: -2px; }
</style>
</head>
<body>
  <main class="cover">
    <div class="cover__band"></div>

    <svg class="cover__shapes" width="848" height="1200" viewBox="0 0 848 1200" aria-hidden="true">
      <defs>
        <linearGradient id="wave-silver" x1="0" y1="0" x2="0" y2="1">
          <stop offset="0" stop-color="#a9a9a9"/>
          <stop offset="0.45" stop-color="#ffffff"/>
          <stop offset="0.75" stop-color="#f2f2f2"/>
          <stop offset="1" stop-color="#a6a6a6"/>
        </linearGradient>
        <linearGradient id="tile-fill" x1="0" y1="0" x2="1" y2="0">
          <stop offset="0.7" stop-color="#176b98"/>
          <stop offset="1" stop-color="#2a8fc4"/>
        </linearGradient>
        <filter id="tile-shadow" x="-20%" y="-20%" width="140%" height="140%">
          <feDropShadow dx="3" dy="6" stdDeviation="5" flood-color="#000" flood-opacity="0.55"/>
        </filter>
      </defs>
      <circle class="shape-circle" cx="130" cy="1100" r="522" fill="var(--ocean)"/>
      <g class="shape-tile" filter="url(#tile-shadow)">
        <rect x="521" y="805" width="235" height="232" rx="56" fill="var(--sky)"/>
        <rect x="531" y="811" width="225" height="226" rx="54" fill="url(#tile-fill)"/>
      </g>
      <path class="shape-wave" d="M0 1126 C 160 1100 300 1062 430 1062 C 600 1062 740 1100 848 1131 L848 1200 L0 1200 Z" fill="url(#wave-silver)"/>
    </svg>

    <div class="brand">
      <span class="brand__mark"></span>
      <span class="brand__name">TALLOWRIDGE</span>
    </div>

    <div class="tagline">
      <svg width="14" height="12" viewBox="0 0 14 12" aria-hidden="true">
        <path d="M1 6 H12 M7.5 1.5 L12 6 L7.5 10.5" stroke="#fff" stroke-width="1.8" fill="none" stroke-linecap="round" stroke-linejoin="round"/>
      </svg>
      <span>Building higher performing organizations.</span>
    </div>

    <h1 class="title title--reasons">5 Reasons</h1>
    <p class="title title--suck">You Suck At</p>
    <p class="title title--fit">Hiring For Fit</p>
  </main>
</body>
</html>
```